Tallowbrook Fitness - Personal & Rehab Training

Business Card for my personal training business - Tallowbrook Fitness. I focus on personal and rehab training. I would like a double sided card, round edges. front of card will be my existing logo and the back will have an image (black and white or exercise, people exercising, weights, etc) along with my name and details. Such as:
Corisse Pembly
Personal & Rehab Trainer
www.tallowbrookfitness.com.au
0438264905
I have some images that I have downloaded that I am happy to send to the designer.
Thanks
Target Market(s)
athletes, middle to high income, sport related
Contact Information for Business Card
Corisse Pembly
Personal & Rehab Trainer
0438264905
Colors
Designer to choose only greyscale colors for use in the design.
Requirements
Must have
- my existing logo
Nice to have
- one of the images uploaded. I really like the girl with the mint coloured shoes as this is one of my logo colours

```html
<!DOCTYPE html>
<html lang="en">
<head>
<meta charset="utf-8">
<title>Tallowbrook Fitness – Business Card</title>
<link href="https://fonts.googleapis.com/css2?family=Montserrat:wght@300;400;500;800&display=swap" rel="stylesheet">
<style>
  :root {
    --page: #1c1c1c;
    --card-dark: #161616;
    --card-dark-edge: #222222;
    --ink-light: #ffffff;
    --ink-soft: #d9d9d9;
    --navy: #1d2a44;
    --mint: #8fe0a8;
    --photo-light: #e6e6e6;
    --photo-mid: #9a9a9a;
    --photo-dark: #4a4a4a;
  }
  * { box-sizing: border-box; margin: 0; padding: 0; }
  html, body { width: 1200px; height: 1200px; overflow: hidden; }
  body {
    background: var(--page);
    font-family: "Montserrat", sans-serif;
    display: flex;
    flex-direction: column;
    align-items: center;
    justify-content: center;
    gap: 60px;
  }
  .card {
    position: relative;
    width: 900px;
    height: 515px;
    border-radius: 34px;
    overflow: hidden;
  }

  /* Photo side */
  .card--photo { background: var(--photo-light); }
  .card__photo {
    position: absolute; inset: 0;
    background:
      radial-gradient(ellipse at 45% 35%, var(--photo-light) 0%, var(--photo-mid) 55%, var(--photo-dark) 100%);
  }
  .card__band {
    position: absolute;
    left: 0; right: 0;
    top: 325px; height: 120px;
    background: rgba(255,255,255,0.6);
    display: flex;
    align-items: center;
    justify-content: center;
    gap: 22px;
  }
  .brand__square {
    width: 58px; height: 58px;
    border: 4px solid currentColor;
    border-radius: 10px;
  }
  .brand__name {
    font-weight: 500;
    font-size: 40px;
    letter-spacing: 0.14em;
    text-transform: uppercase;
    line-height: 1;
  }
  .card--photo .brand { color: var(--navy); }

  /* Details side */
  .card--details {
    background: linear-gradient(160deg, var(--card-dark-edge), var(--card-dark));
    color: var(--ink-light);
  }
  .card--details .brand {
    position: absolute;
    left: 0; right: 0; top: 150px;
    display: flex; align-items: center; justify-content: center;
    gap: 26px;
  }
  .card--details .brand__square { width: 84px; height: 84px; border-width: 5px; border-radius: 14px; }
  .card--details .brand__name { font-size: 46px; }
  .contact {
    position: absolute;
    left: 210px; top: 360px;
  }
  .contact__headline { display: flex; align-items: baseline; gap: 18px; }
  .contact__name {
    font-weight: 800;
    font-size: 30px;
    letter-spacing: 0.03em;
    text-transform: uppercase;
  }
  .contact__role { font-weight: 300; font-size: 20px; color: var(--ink-soft); }
  .contact__lines {
    display: flex; gap: 28px; margin-top: 12px;
    font-weight: 300; font-size: 20px; color: var(--ink-soft);
  }
  .contact__item { display: flex; align-items: center; gap: 8px; }
  .contact__icon { width: 20px; height: 20px; }
</style>
</head>
<body>

  <section class="card card--photo">
    <div class="card__photo" role="img" aria-label="Black and white photo of people training in a gym"></div>
    <div class="card__band">
      <div class="brand">
        <div style="display:flex;align-items:center;gap:22px;">
          <span class="brand__square"></span>
          <span class="brand__name">Tallowbrook Fitness</span>
        </div>
      </div>
    </div>
  </section>

  <section class="card card--details">
    <div class="brand">
      <span class="brand__square"></span>
      <span class="brand__name">Tallowbrook Fitness</span>
    </div>
    <div class="contact">
      <div class="contact__headline">
        <span class="contact__name">Corisse Pembly</span>
        <span class="contact__role">Personal &amp; Rehab Trainer</span>
      </div>
      <div class="contact__lines">
        <span class="contact__item">
          <svg class="contact__icon" viewBox="0 0 24 24" aria-hidden="true">
            <path fill="var(--mint)" d="M6.6 10.8a15.1 15.1 0 0 0 6.6 6.6l2.2-2.2a1 1 0 0 1 1-.25 11.4 11.4 0 0 0 3.6.57 1 1 0 0 1 1 1V20a1 1 0 0 1-1 1A17 17 0 0 1 3 4a1 1 0 0 1 1-1h3.5a1 1 0 0 1 1 1c0 1.25.2 2.45.57 3.57a1 1 0 0 1-.25 1z"/>
          </svg>
          0438264905
        </span>
        <span class="contact__item">
          <svg class="contact__icon" viewBox="0 0 24 24" aria-hidden="true" fill="none" stroke="var(--mint)" stroke-width="1.6">
            <circle cx="12" cy="12" r="9"/>
            <ellipse cx="12" cy="12" rx="4" ry="9"/>
            <line x1="3" y1="12" x2="21" y2="12"/>
          </svg>
          www.tallowbrookfitness.com.au
        </span>
      </div>
    </div>
  </section>

</body>
</html>
```